Bref créative
Olive Oil and Balsamic Vinegar Company
Lomisca
- I am looking for a modern label for my Olive oil and Balsamics.
- The parameter for the label is 2" by 4"
- I want a classic looking but edgey label. The bottled cost 23.99 so it has to show time was spend into the design.
- They are imported from Italy so i need some resemblence to italy but not the green, red, white color scheme.
- The name of the oils "Lomisca" i want in a cursive type writing but with the "F" to be a bigger with loop type font you can say.
Food
Im a wholeseller and a personal seller so i have a wind target of customer from corporate to normal day people.
I need to be able to edit the texts so i can add history and change the name of the flavors.
Contact me if need clarification or more details
Example 2 I really like
Example 1 I really like

```html
<!DOCTYPE html>
<html lang="en">
<head>
<meta charset="utf-8">
<title>Lomisca — Label Set</title>
<link href="https://fonts.googleapis.com/css2?family=Cinzel:wght@400;600&family=Cormorant+Garamond:ital,wght@1,500;1,600&display=swap" rel="stylesheet">
<style>
  :root {
    --olive-deep: #123f14;
    --olive-dark: #0b2e0d;
    --lime: #bccf2f;
    --lime-soft: #d4e04a;
    --gold: #e3d63a;
    --cream: #f4f1d8;
    --page: #ffffff;
  }
  * { margin: 0; padding: 0; box-sizing: border-box; }
  html, body { width: 1200px; height: 872px; overflow: hidden; background: var(--page); }
  .canvas {
    position: relative; width: 1200px; height: 872px;
    display: flex; justify-content: center; align-items: center; gap: 44px;
  }
  .label {
    position: relative; width: 330px; height: 760px;
    display: flex; flex-direction: column; align-items: center; text-align: center;
    font-family: "Cinzel", serif;
  }
  .label__shape { position: absolute; inset: 0; width: 330px; height: 760px; }
  .label > *:not(.label__shape) { position: relative; }

  .brand {
    margin-top: 170px; display: flex; align-items: center; gap: 12px;
  }
  .brand__dot { width: 34px; height: 34px; border-radius: 50%; }
  .brand__name { font-family: "Cinzel", serif; font-weight: 400; font-size: 50px; letter-spacing: 1px; }

  .product { margin-top: 150px; line-height: 1.05; }
  .product__kind { font-size: 34px; letter-spacing: 1px; }
  .product__name { font-size: 44px; letter-spacing: 1px; }
  .product__joiner { font-family: "Cormorant Garamond", serif; font-style: italic; font-weight: 600; font-size: 36px; text-transform: none; }

  .product__italian {
    margin-top: 34px; font-family: "Cormorant Garamond", serif; font-style: italic; font-weight: 600;
    font-size: 20px; letter-spacing: 1.5px; text-transform: uppercase; line-height: 1.2;
  }
  .volume { margin-top: auto; margin-bottom: 46px; font-size: 14px; letter-spacing: 1px; text-transform: none; }

  .label--oil { color: var(--cream); }
  .label--oil .brand__name { color: var(--lime); }
  .label--oil .brand__dot { background: var(--lime-soft); }
  .label--oil .product__italian { color: var(--gold); }

  .label--vinegar { color: var(--olive-deep); }
  .label--vinegar .brand__name { color: var(--olive-deep); }
  .label--vinegar .brand__dot { background: var(--olive-deep); }
  .label--vinegar .product__italian { color: var(--cream); }
</style>
</head>
<body>
<main class="canvas">
  <section class="label label--oil">
    <svg class="label__shape" viewBox="0 0 330 760" aria-hidden="true">
      <path d="M0 760 V110 C0 40 60 0 165 0 C270 0 330 40 330 110 V760 Z" fill="var(--olive-deep)"/>
      <path d="M14 746 V114 C14 52 70 14 165 14 C260 14 316 52 316 114 V746 Z" fill="none" stroke="var(--lime)" stroke-width="3"/>
    </svg>
    <div class="brand"><span class="brand__dot"></span><span class="brand__name">Lomisca</span></div>
    <h2 class="product">
      <span class="product__kind">Extra Virgin</span><br>
      <span class="product__name">Olive Oil</span>
    </h2>
    <p class="product__italian">Olio extra vergine<br>di oliva</p>
    <p class="volume">250ml</p>
  </section>

  <section class="label label--vinegar">
    <svg class="label__shape" viewBox="0 0 330 760" aria-hidden="true">
      <path d="M0 760 V110 C0 40 60 0 165 0 C270 0 330 40 330 110 V760 Z" fill="var(--lime)"/>
      <path d="M14 746 V114 C14 52 70 14 165 14 C260 14 316 52 316 114 V746 Z" fill="none" stroke="var(--olive-deep)" stroke-width="3"/>
    </svg>
    <div class="brand"><span class="brand__dot"></span><span class="brand__name">Lomisca</span></div>
    <h2 class="product">
      <span class="product__kind">Balsamic</span><br>
      <span class="product__name">Vinegar</span><br>
      <span class="product__kind"><span class="product__joiner">of</span> Modena</span>
    </h2>
    <p class="product__italian">Aceto balsamico<br>di Modena</p>
    <p class="volume">250ml</p>
  </section>
</main>
</body>
</html>
```